Consultancy Business Card Design

We need a business card design for a new company based in singapore called FortyOne. FortyOne a boutique consultancy firm offering broad-based business solutions, from conception to re-invention, for ventures from new start-ups to long-running traditional businesses.
Its 2 main divisions (Food & Beverage Operations and Construction & Project Management) have access to a wide range of networks, knowledge bases, and resources to service its clients across numerous diverse sectors. This includes, and is not limited to, construction, F&B, and retail.
We are a company that combines the ambition, boldness and energy of one in the 20s with the dedication, level-headedness and dependability of one entering its 30s. Bridging the experiences of the old with ideals of the young, we draw on the positives of both to create a unique synergy.
We hope to see designs that fits our company profile.
Boutique
FortyOne(Company Name)
Marcus Leow (Name)
Principle Consultant (Title)
F&B and Hospitality (Division)
(+65) 8364 5170 (Contact no.)
marcus@fortyone-example.com.sg (Email)

```html
<!DOCTYPE html>
<html lang="en">
<head>
<meta charset="utf-8">
<title>FortyOne — Business Card</title>
<link rel="stylesheet" href="https://fonts.googleapis.com/css2?family=Montserrat:wght@400;500;600&display=swap">
<style>
  :root {
    --canvas: #2a2a2c;
    --card: #161617;
    --card-glow: #252527;
    --red: #ee2e2e;
    --red-soft: #f04848;
    --white: #f1f1f1;
    --grey: #b9b9bb;
  }
  * { box-sizing: border-box; margin: 0; padding: 0; }
  html, body {
    width: 1200px; height: 900px; overflow: hidden;
    background: var(--canvas);
    font-family: "Montserrat", Arial, sans-serif;
  }
  .stage {
    width: 1200px; height: 900px;
    display: flex; flex-direction: column; align-items: center; justify-content: center;
    gap: 40px;
  }
  .card {
    position: relative;
    width: 660px; height: 378px;
    background: radial-gradient(ellipse at 55% 40%, var(--card-glow) 0%, var(--card) 70%);
    overflow: hidden;
    box-shadow: 0 10px 30px rgba(0,0,0,.45);
  }
  .band { position: absolute; left: 0; right: 0; background: var(--red); }
  .band--thick-top { top: 0; height: 16px; }
  .band--thin-bottom { bottom: 0; height: 6px; }
  .band--thick-bottom { bottom: 0; height: 16px; }

  .wordmark {
    position: absolute; left: 0; right: 0;
    display: flex; align-items: center; justify-content: center; gap: 16px;
    font-weight: 500; font-size: 36px; letter-spacing: 8px;
    text-transform: uppercase;
    color: var(--white);
  }
  .wordmark__mark {
    width: 14px; height: 14px; background: var(--red); flex: none;
  }
  .card--front .wordmark { top: 108px; }
  .card--back .wordmark { top: 162px; }

  .contacts {
    position: absolute; left: 36px; right: 36px; bottom: 40px;
    display: grid; grid-template-columns: 1fr 1fr 1.25fr; align-items: start;
  }
  .contact { display: flex; flex-direction: column; align-items: center; text-align: center; gap: 12px; }
  .contact__icon { width: 26px; height: 26px; }
  .contact__text { font-size: 12.5px; line-height: 1.55; color: var(--grey); }
  .contact__text--strong { color: var(--white); letter-spacing: 0.6px; }
  .contact__title { color: var(--red-soft); font-weight: 500; }
</style>
</head>
<body>
<main class="stage">

  <section class="card card--front" aria-label="Card front">
    <div class="band band--thick-top"></div>
    <h1 class="wordmark"><span class="wordmark__mark" aria-hidden="true"></span>Fortyone</h1>

    <div class="contacts">
      <div class="contact">
        <svg class="contact__icon" viewBox="0 0 26 26" aria-hidden="true">
          <rect x="1" y="1" width="24" height="24" fill="none" stroke="var(--red)" stroke-width="1.5"/>
          <circle cx="13" cy="10" r="3.4" fill="var(--red)"/>
          <path d="M7 19.5c0-3.4 2.7-5.3 6-5.3s6 1.9 6 5.3z" fill="var(--red)"/>
        </svg>
        <p class="contact__text">
          Marcus Leow<br>
          <span class="contact__title">Principle Consultant -</span><br>
          F&amp;B and Hospitality
        </p>
      </div>

      <div class="contact">
        <svg class="contact__icon" viewBox="0 0 26 26" aria-hidden="true">
          <rect x="1" y="1" width="24" height="24" fill="none" stroke="var(--red)" stroke-width="1.5"/>
          <path d="M9.2 7.5l2 2.4-1.2 1.6c.8 1.8 2.1 3.2 3.9 4.1l1.6-1.2 2.4 2-1.3 1.9c-4.6-.6-8.4-4.4-9-9z" fill="var(--red)"/>
        </svg>
        <p class="contact__text contact__text--strong">(+65) 8364 5170</p>
      </div>

      <div class="contact">
        <svg class="contact__icon" viewBox="0 0 26 26" aria-hidden="true">
          <rect x="1" y="1" width="24" height="24" fill="none" stroke="var(--red)" stroke-width="1.5"/>
          <rect x="7" y="9" width="12" height="8.5" fill="var(--red)"/>
          <path d="M7 9l6 4.6L19 9" fill="none" stroke="var(--card)" stroke-width="1.2"/>
        </svg>
        <p class="contact__text">marcus@fortyone-example.com.sg</p>
      </div>
    </div>

    <div class="band band--thin-bottom"></div>
  </section>

  <section class="card card--back" aria-label="Card back">
    <h2 class="wordmark"><span class="wordmark__mark" aria-hidden="true"></span>Fortyone</h2>
    <div class="band band--thick-bottom"></div>
  </section>

</main>
</body>
</html>
```